Trade-show Exhibit Booth Main 8' x 8' Graphic Design

Our company, Harbor-Line Ledger Corporation, is seeking a new design for our trade Show Exhibit Booth graphic panel (made of fabric).  As a consulting and software company, we are looking for a very high-end, professional  design concept.
The booth backdrop is a dye sublimated fabric with grommets, hung with a large truss kit.  Here is a link to an image of our exhibit booth: http://www.examplebannerworks.com/images/vendra/qx7-2_2_lrg.jpg
We will need two backdrop designs.  Each of the designs will be basically the same, but in two different sizes.
Fabric dimensions are:
- 102”w x 109.5”h
- 102"w x 85" h
There is a 2½ feet wide strip of “dead space” that runs horizontally left to right  along the bottom of the graphic.  This is because the bottom of the display is hard to view due to the front table.  This area along the bottom is not very visible due to table front. We do need print on this space, but the important area of the design should be above this area.
OUR GOAL FOR THE GRAPHIC YOU SUBMIT
We would like to convey that we offer 4 distinct business units.  Two Business units come under our consulting company and two come under our software.  However, we now want to combine the two companies and websites so we can market them all together.
The backdrop for the Display Booth convey the following ideas:
1. Have a very high end professional look, such as law firm or professional consulting group might have.
2. We envisioned 4 graphics that show those areas of business brought together in the center by our company HLLC.  However, we are open to any ideas.
3. We ask that you don’t use Puzzle pieces or mazes as there are so many graphics of that type on other booths.
4. Our key colors can be found on our two attached logos
a. HLLC is our main company logo
b. BrightVault is our software logo that should be in one of the areas of business
5. Also, our logo looks best on a black background.
6. The graphic should show how the following 4 areas of business are offered by our single company, HLLC.   The Areas of Business are as follows:
a. Consulting
b. Software
c. FTZ Implementation and Operation
d. FTZ Administration
7. Keep in mind it is important to show the software portion.
8. Also, as a note, our company helps U.S. Based Firms involved in international trade save money on Customs Duty.
Here is the link to our logos: http://www.hllsystems.example/filetransfer/upload/dropbox/131111logosforclientproject.zip
We have two websites that we plan on combining into one.  The websites will help you lean about our company.
www.hllcorp.example
www.hllsystems.example

Updates
I have increased the 1st place to $700 and made the project non refundable.  Please submit a design as we have a great deal of other projects to complets.

PLEASE NOTE: We no longer use the BrightVault logo. We have a new version, but there is no need to ad that now. Please do not include the BrightVault logo in your designs unless we provide the updated one directly to you.
Thanks,
Dennis
I have updated a copy of our Logo. If you need an EPS copy, please message me and I will send you an EPS copy of the logo.
Also I have raised $$ amount o the 1st, 2nd, and 3rd place files, and they are guaranteed.
Thank you all for your designs.
Reason: I have extended the deadline by one day so the designers can submit any modifications they have in mind.

Target Market(s)
Directors, Vice Presidents and CEO's of medium to large corporations.   The individuals we sell our services and software to want to make sure their project goes smooth and they want to hire a company that looks professional.
We deal mostly with Director and Vice President Level individuals at medium to the very largest companies.
Industry/Entity Type
Software
Requirements
Must have
- Professional image
Bold eye catching look
Should not have
- Puzzle pieces
Mazes

```html
<!DOCTYPE html>
<html lang="en">
<head>
<meta charset="utf-8">
<title>HLLC Exhibit Booth Backdrop</title>
<link rel="stylesheet" href="https://fonts.googleapis.com/css2?family=Source+Sans+3:wght@400&display=swap">
<style>
  :root {
    --page-bg: #e6e3df;
    --panel-black: #000000;
    --panel-mid: #5b5b5e;
    --panel-light: #a4a5a8;
    --panel-white: #ffffff;
    --banner-white: #ffffff;
    --banner-shadow: #3a3a3c;
    --brand-green: #8cc63f;
    --brand-green-soft: #b5d98a;
    --globe-light: #f6f6f6;
    --globe-shade: #d2d2d2;
  }
  html, body {
    margin: 0;
    padding: 0;
    width: 1200px;
    height: 1000px;
    overflow: hidden;
    background: var(--page-bg);
  }
  .canvas {
    position: relative;
    width: 1200px;
    height: 1000px;
  }
  .backdrop {
    position: absolute;
    left: 187px;
    top: 36px;
    width: 885px;
    height: 945px;
    background: linear-gradient(to bottom,
      var(--panel-black) 0%,
      var(--panel-black) 17%,
      var(--panel-mid) 33%,
      var(--panel-light) 65%,
      var(--panel-white) 100%);
    overflow: hidden;
  }
  .backdrop svg {
    position: absolute;
    left: 0;
    top: 0;
  }
  .service-banner { fill: var(--banner-white); }
  .service-shadow { fill: var(--banner-shadow); }
  .service-label {
    font-family: "Source Sans 3", sans-serif;
    font-weight: 400;
    fill: var(--brand-green);
  }
  .brand-mark {
    position: absolute;
    right: 2px;
    top: 8px;
    width: 156px;
    height: 124px;
    background: var(--panel-black);
    display: flex;
    align-items: center;
    justify-content: center;
  }
  .brand-name {
    font-family: "Source Sans 3", sans-serif;
    font-weight: 400;
    font-size: 54px;
    letter-spacing: 4px;
    color: var(--brand-green);
  }
</style>
</head>
<body>
<div class="canvas">
  <div class="backdrop">
    <svg width="885" height="945" viewBox="0 0 885 945" xmlns="http://www.w3.org/2000/svg">
      <defs>
        <radialGradient id="globeFill" cx="45%" cy="45%" r="62%">
          <stop offset="0%" stop-color="var(--globe-light)"/>
          <stop offset="45%" stop-color="#e9efe0"/>
          <stop offset="75%" stop-color="var(--brand-green-soft)"/>
          <stop offset="100%" stop-color="var(--brand-green)"/>
        </radialGradient>
      </defs>

      <g class="service consulting">
        <polygon class="service-shadow" points="168,80 660,122 660,215 222,214"/>
        <polygon class="service-banner" points="171,82 670,122 670,206 225,211"/>
        <text class="service-label" x="250" y="158" font-size="50" transform="rotate(4 250 158)">Consulting</text>
      </g>
      <g class="service software">
        <polygon class="service-shadow" points="120,209 470,224 470,342 175,342"/>
        <polygon class="service-banner" points="123,211 480,224 480,332 178,338"/>
        <text class="service-label" x="195" y="288" font-size="48" transform="rotate(3 195 288)">Software</text>
      </g>
      <g class="service administration">
        <polygon class="service-shadow" points="38,333 440,362 440,460 92,466"/>
        <polygon class="service-banner" points="41,335 450,362 450,450 95,462"/>
        <text class="service-label" x="76" y="412" font-size="42" transform="rotate(3 76 412)">FTZ Administration</text>
      </g>
      <g class="service implementation">
        <polygon class="service-shadow" points="3,466 600,500 600,582 58,600"/>
        <polygon class="service-banner" points="6,468 610,500 610,574 61,596"/>
        <text class="service-label" x="50" y="528" font-size="42">FTZ Implementation</text>
        <text class="service-label" x="113" y="574" font-size="42">and Operation</text>
      </g>

      <circle cx="652" cy="360" r="240" fill="var(--banner-shadow)"/>
      <circle cx="650" cy="356" r="236" fill="url(#globeFill)" role="img"
        aria-label="Globe illustration with green continents of the Americas, Europe and Africa on a white sphere"/>
    </svg>

    <div class="brand-mark">
      <span class="brand-name">HLLC</span>
    </div>
  </div>
</div>
</body>
</html>
```